Business Card and Letterhead for new company Vardel GreenWorks, Inc.

Vardel GreenWorks, Inc., an engineering and construction firm that provides services for solid waste landfill gas systems, needs a business card and letterhead. We recently had a logo designed but we are open to some tweaks to logo design and color scheme. Generally, we like "earthy" color tones - greens, browns, oranges. This is a sister company - www.talvoriengineering.example.

Target Market(s)

Solid waste landfill companies - Brindle Disposal, Halcott Hauling, etc.

Industry/Entity Type

Engineering and Construction

Contact Information for Business Card

Name, Title, email, mobile phone, work phone, website. Potential list of services for back of card: LFG Engineering and Design, GCCS Planning and Operational Consulting, Compliance Monitoring and Reporting, Routine Operations & Maintenance, Nonroutine O&M, Construction Management, Construction QA, GCCS Construction

Font styles to use
Sans Serif

Requirements
Must have
• Logo, pertinent information, maybe a tagline (still in development)
Nice to have
• For back of card, considering an engineering scale (attached for another business of ours), but want to look at other options, alternatives. Like the idea of the back of card to have some utility (scale, unit conversion info, list of services) but willing to consider lots of options.
Should not have
• Needs to have a professional (engineering) and technical look, not cartoonish.

```html
<!DOCTYPE html>
<html lang="en">
<head>
<meta charset="utf-8">
<title>Vardel GreenWorks – Letterhead and Business Card</title>
<link href="https://fonts.googleapis.com/css2?family=Inter:ital,wght@0,400;0,500;0,600;1,400&display=swap" rel="stylesheet">
<style>
  :root {
    --backdrop: #f1f1f2;
    --paper: #ffffff;
    --green: #76b543;
    --earth: #6f6446;
    --ink: #222222;
    --muted: #6f6446;
    --faint: #f3f4f3;
  }
  * { margin: 0; padding: 0; box-sizing: border-box; }
  html, body { width: 1200px; height: 900px; overflow: hidden; }
  body {
    background: var(--backdrop);
    font-family: "Inter", Arial, sans-serif;
    color: var(--ink);
    position: relative;
  }

  /* Letterhead */
  .letterhead {
    position: absolute; left: 206px; top: 52px;
    width: 564px; height: 797px;
    background: var(--paper);
    box-shadow: 3px 4px 6px rgba(0,0,0,.18);
    overflow: hidden;
  }
  .letterhead .band-green { position: absolute; left: 0; top: 0; width: 41px; height: 665px; background: var(--green); }
  .letterhead .band-earth { position: absolute; left: 0; top: 665px; width: 41px; height: 132px; background: var(--earth); }
  .letterhead .backdrop-mark {
    position: absolute; left: 366px; top: 80px; width: 170px; height: 170px;
    border-radius: 50%; background: var(--faint);
  }
  .brand {
    position: absolute; display: flex; align-items: center; gap: 8px;
    color: var(--green); font-weight: 600; white-space: nowrap;
  }
  .brand .dot { border-radius: 50%; background: var(--green); flex: none; }
  .letterhead .brand { left: 67px; top: 70px; font-size: 21px; }
  .letterhead .brand .dot { width: 26px; height: 26px; }

  .recipient, .dateline { position: absolute; top: 164px; font-size: 11px; line-height: 14px; }
  .recipient { left: 74px; }
  .dateline { right: 34px; text-align: right; }
  .recipient .label, .dateline .label { display: block; margin-bottom: 11px; }
  .recipient .name, .dateline .date { display: block; font-weight: 600; margin-bottom: 8px; }

  .letter-body {
    position: absolute; left: 74px; top: 272px; width: 456px;
    font-size: 11.4px; line-height: 13.65px; text-align: justify;
  }
  .letter-body p { margin-bottom: 13.65px; }

  .signoff {
    position: absolute; right: 81px; top: 601px;
    font-size: 11px; line-height: 14px; text-align: right;
  }

  .letter-footer {
    position: absolute; left: 74px; top: 724px;
    font-size: 8px; color: var(--muted);
  }
  .letter-footer li { list-style: none; display: flex; align-items: center; height: 14px; }
  .letter-footer svg { width: 11px; height: 11px; margin-right: 8px; flex: none; }
  .letter-footer .company { padding-left: 19px; }

  /* Business card front */
  .card {
    position: absolute; left: 790px; width: 205px; height: 123px;
    box-shadow: 3px 4px 6px rgba(0,0,0,.2); overflow: hidden;
  }
  .card-front { top: 52px; background: var(--paper); }
  .card-front .edge-green { position: absolute; right: 0; top: 0; width: 4px; height: 103px; background: var(--green); }
  .card-front .edge-earth { position: absolute; right: 0; top: 103px; width: 4px; height: 20px; background: var(--earth); }
  .card-front .backdrop-mark {
    position: absolute; left: 8px; top: 38px; width: 62px; height: 62px;
    border-radius: 50%; background: var(--faint);
  }
  .card-front .brand { left: 10px; top: 12px; font-size: 9px; gap: 4px; }
  .card-front .brand .dot { width: 11px; height: 11px; }
  .card-front .person { position: absolute; right: 22px; top: 44px; text-align: right; }
  .card-front .person .name { color: var(--green); font-size: 8.6px; display: block; }
  .card-front .person .title { font-style: italic; font-size: 4.4px; color: var(--muted); display: block; margin-top: 2px; }
  .card-front .contacts { position: absolute; right: 22px; top: 78px; font-size: 4.4px; color: var(--muted); }
  .card-front .contacts li { list-style: none; display: flex; justify-content: flex-end; align-items: center; height: 9px; }
  .card-front .contacts svg { width: 5px; height: 5px; margin-left: 6px; }

  /* Business card back */
  .card-back { top: 195px; background: var(--earth); }
  .card-back h2 { position: absolute; left: 20px; top: 19px; font-size: 8.5px; font-weight: 400; color: var(--green); }
  .card-back ul { position: absolute; left: 20px; top: 34px; }
  .card-back li { list-style: none; color: #fff; font-size: 5.5px; line-height: 9.1px; }
  .ruler { position: absolute; right: 0; top: 0; width: 40px; height: 123px; }
</style>
</head>
<body>

<main class="letterhead">
  <div class="band-green"></div>
  <div class="band-earth"></div>
  <div class="backdrop-mark" aria-hidden="true"></div>

  <div class="brand"><span class="dot"></span>Vardel GreenWorks</div>

  <div class="recipient">
    <span class="label">TO :</span>
    <span class="name">Mr. Smith</span>
    Marketing Manager<br>Company
  </div>
  <div class="dateline">
    <span class="label">DATE :</span>
    <span class="date">AUGUST 18, 2024</span>
  </div>

  <div class="letter-body">
    <p>Lorem ipsum dolor sit amet, consectetuer adipiscing elit, sed diam nonummy nibh euismod tincidunt ut laoreet dolore magna aliquam erat volutpat. Ut wisi enim ad minim veniam, quis nostrud exerci tation ullamcorper suscipit lobortis nisl ut aliquip ex ea commodo consequat. Duis autem vel eum iriure dolor in hendrerit in vulputate velit esse molestie consequat, vel illum dolore eu feugiat nulla facilisis at vero eros et accumsan et iusto odio dignissim qui blandit praesent luptatum zzril delenit augue duis dolore te feugait nulla facilisi.</p>
    <p>Lorem ipsum dolor sit amet, cons ectetuer adipiscing elit, sed diam nonummy nibh euismod tincidunt ut laoreet dolore magna aliquam erat volutpat. Ut wisi enim ad minim veniam, quis nostrud exerci tation ullamcorper suscipit lobortis nisl ut aliquip ex ea commodo consequat.</p>
    <p>Lorem ipsum dolor sit amet, consectetuer adipiscing elit, sed diam nonummy nibh euismod tincidunt ut laoreet dolore magna aliquam erat volutpat. Ut wisi enim ad minim veniam, quis nostrud exerci tation ullamcorper suscipit lobortis nisl ut aliquip ex ea commodo consequat. Duis autem vel eum iriure dolor in hendrerit in vulputate velit esse molestie consequat, vel illum dolore eu feugiat nulla facilisis at vero eros et accumsan et iusto odio dignissim qui blandit praesent luptatum zzril delenit augue duis dolore te feugait nulla facilisi.veniam, quis nostrud exerci tation ullamcorper suscipit lobortis nisl ut aliquip ex ea commodo consequat.</p>
  </div>

  <div class="signoff">Sincerly,<br>HRD Manager</div>

  <ul class="letter-footer">
    <li class="company">Vardel GreenWorks, Inc.</li>
    <li>
      <svg viewBox="0 0 12 12"><path d="M6 1a3.8 3.8 0 0 0-3.8 3.8C2.2 7.6 6 11 6 11s3.8-3.4 3.8-6.2A3.8 3.8 0 0 0 6 1z" fill="none" stroke="#76b543" stroke-width="1.2"/><circle cx="6" cy="4.8" r="1.3" fill="#76b543"/></svg>
      480 Quarry Ridge Road, Suite 210, Millbrook, TN, 37000, United States
    </li>
    <li>
      <svg viewBox="0 0 12 12"><path d="M2.5 1.5l2 .2 1 2.4-1.3 1a6 6 0 0 0 2.7 2.7l1-1.3 2.4 1 .2 2a1 1 0 0 1-1 1A9 9 0 0 1 1.5 2.5a1 1 0 0 1 1-1z" fill="none" stroke="#76b543" stroke-width="1.1"/></svg>
      555-010-4417
    </li>
    <li>
      <svg viewBox="0 0 12 12"><g fill="none" stroke="#76b543" stroke-width="1.1"><circle cx="6" cy="6" r="5"/><ellipse cx="6" cy="6" rx="2.2" ry="5"/><path d="M1 6h10M2 3.5h8M2 8.5h8"/></g></svg>
      www.vardelgreenworks.example
    </li>
  </ul>
</main>

<section class="card card-front">
  <div class="backdrop-mark" aria-hidden="true"></div>
  <div class="brand"><span class="dot"></span>Vardel GreenWorks</div>
  <div class="person">
    <span class="name">Dorian K. Fellowes, PE</span>
    <span class="title">President, Principal Engineer</span>
  </div>
  <ul class="contacts">
    <li>555-010-4417<svg viewBox="0 0 12 12"><path d="M2.5 1.5l2 .2 1 2.4-1.3 1a6 6 0 0 0 2.7 2.7l1-1.3 2.4 1 .2 2a1 1 0 0 1-1 1A9 9 0 0 1 1.5 2.5a1 1 0 0 1 1-1z" fill="#76b543"/></svg></li>
    <li>555-010-7720<svg viewBox="0 0 12 12"><rect x="3" y="1" width="6" height="10" rx="1" fill="none" stroke="#76b543" stroke-width="1.5"/></svg></li>
    <li>dfellowes@vardelgreenworks.example<svg viewBox="0 0 12 12"><rect x="1" y="2.5" width="10" height="7" fill="none" stroke="#76b543" stroke-width="1.4"/><path d="M1 2.5l5 4 5-4" fill="none" stroke="#76b543" stroke-width="1.2"/></svg></li>
    <li>www.vardelgreenworks.example<svg viewBox="0 0 12 12"><circle cx="6" cy="6" r="5" fill="#76b543"/></svg></li>
  </ul>
  <div class="edge-green"></div>
  <div class="edge-earth"></div>
</section>

<section class="card card-back">
  <h2>SERVICES</h2>
  <ul>
    <li>• LFG Engineering and Design</li>
    <li>• GCCS Planning and Operational Consulting</li>
    <li>• Compliance Monitoring and Reporting</li>
    <li>• Routine Operations &amp; Maintenance</li>
    <li>• Nonroutine O&amp;M</li>
    <li>• Construction Management</li>
    <li>• Construction QA</li>
    <li>• GCCS Construction</li>
  </ul>
  <svg class="ruler" viewBox="0 0 40 123" aria-label="Centimetre scale">
    <defs>
      <pattern id="mm-ticks" width="40" height="2.2" patternUnits="userSpaceOnUse" y="7">
        <line x1="34" y1="0.3" x2="40" y2="0.3" stroke="#fff" stroke-width="0.4"/>
      </pattern>
    </defs>
    <rect x="0" y="7" width="40" height="110" fill="url(#mm-ticks)"/>
    <g stroke="#fff" stroke-width="0.5">
      <line x1="20" y1="7.3" x2="40" y2="7.3"/>
      <line x1="20" y1="29.3" x2="40" y2="29.3"/>
      <line x1="20" y1="51.3" x2="40" y2="51.3"/>
      <line x1="20" y1="73.3" x2="40" y2="73.3"/>
      <line x1="20" y1="95.3" x2="40" y2="95.3"/>
      <line x1="20" y1="117.3" x2="40" y2="117.3"/>
    </g>
    <g fill="#fff" font-family="Inter, Arial, sans-serif" font-size="3.6" text-anchor="middle">
      <text transform="translate(15 8) rotate(90)">cm</text>
      <text transform="translate(15 29) rotate(90)">1</text>
      <text transform="translate(15 51) rotate(90)">2</text>
      <text transform="translate(15 73) rotate(90)">3</text>
      <text transform="translate(15 95) rotate(90)">4</text>
      <text transform="translate(15 117) rotate(90)">5</text>
    </g>
  </svg>
</section>

</body>
</html>
```